Business Card Design

Business Card for professional consulting firm working with large financial institutions.

Target Market(s)

Executive buyers

Industry/Entity Type

Banking

Contact Information for Business Card

Mild creativity wanted. Not boring, but do elaborate artwork.

Font styles to use
Serif
Sans Serif

Colors

Designer to choose colors to be used in the design.

Requirements
Must have
• Standard business card features - company name, individual name, telephone, website, email, locations.
Nice to have
• Two colors
Should not have
• too many colors, fancy printing, cartoons.

```html
<!DOCTYPE html>
<html lang="en">
<head>
<meta charset="utf-8">
<title>Meridell Business Card</title>
<link rel="stylesheet" href="https://fonts.googleapis.com/css2?family=EB+Garamond:wght@400;500;600&display=swap">
<style>
  :root {
    --bg: #3a3a3a;
    --card-back: #b3b3b3;
    --card-front: #ffffff;
    --ink: #1e1e1e;
    --ink-soft: #2f2f2f;
    --accent-grey: #bdbdbd;
    --icon-grey: #8a8a8a;
  }
  * { margin: 0; padding: 0; box-sizing: border-box; }
  html, body { width: 1200px; height: 1000px; overflow: hidden; }
  body {
    background: var(--bg);
    font-family: "EB Garamond", Georgia, serif;
    color: var(--ink);
    position: relative;
  }
  .card {
    position: absolute;
    left: 280px;
    width: 640px;
    height: 366px;
    border-radius: 22px;
    overflow: hidden;
  }
  .card--back { top: 90px; background: var(--card-back); }
  .card--front { top: 520px; background: var(--card-front); }

  .wordmark {
    position: absolute;
    font-family: "EB Garamond", Georgia, serif;
    font-weight: 500;
    color: var(--ink);
    letter-spacing: 1px;
    white-space: nowrap;
    display: flex;
    align-items: center;
    gap: 14px;
  }
  .wordmark__dot { width: 12px; height: 12px; border-radius: 50%; background: var(--ink); }
  .card--back .wordmark { font-size: 64px; left: 50%; top: 50%; transform: translate(-50%, -50%); }
  .card--front .wordmark { font-size: 44px; left: 370px; top: 120px; }
  .card--front .wordmark__dot { width: 9px; height: 9px; }

  .edge-tab {
    position: absolute; left: 0; top: 42px;
    width: 10px; height: 56px;
    background: var(--accent-grey);
    border-radius: 0 4px 4px 0;
  }
  .holder { position: absolute; left: 34px; top: 44px; }
  .holder__name { font-size: 22px; font-weight: 500; letter-spacing: 0.5px; text-transform: uppercase; line-height: 1; }
  .holder__title { font-size: 11px; font-weight: 600; letter-spacing: 0.6px; text-transform: uppercase; margin-top: 4px; }

  .contact { position: absolute; left: 34px; top: 220px; font-size: 15px; font-weight: 500; color: var(--ink-soft); line-height: 1.4; }
  .contact__row { display: flex; align-items: flex-start; gap: 8px; }
  .contact__row + .contact__row { margin-top: 4px; }
  .contact__icon { width: 13px; height: 13px; flex: none; margin-top: 3px; fill: var(--icon-grey); }

  .band { position: absolute; background: var(--accent-grey); height: 16px; }
  .band--left { left: 0; top: 322px; width: 380px; }
  .band--right { right: 0; top: 338px; width: 110px; }
  .website { position: absolute; left: 392px; top: 318px; font-size: 16px; font-weight: 600; letter-spacing: 0.4px; }
</style>
</head>
<body>
  <section class="card card--back" aria-label="Card back">
    <div class="wordmark"><span>meridell</span><span class="wordmark__dot"></span></div>
  </section>

  <section class="card card--front" aria-label="Card front">
    <div class="edge-tab"></div>
    <div class="holder">
      <p class="holder__name">Daniel Hartwell</p>
      <p class="holder__title">General Manager</p>
    </div>

    <div class="wordmark"><span>meridell</span><span class="wordmark__dot"></span></div>

    <div class="contact">
      <div class="contact__row">
        <svg class="contact__icon" viewBox="0 0 12 12"><path d="M6 0a4 4 0 0 0-4 4c0 3 4 8 4 8s4-5 4-8a4 4 0 0 0-4-4zm0 5.5A1.5 1.5 0 1 1 6 2.5a1.5 1.5 0 0 1 0 3z"/></svg>
        <span>48 Westbrook Plaza Harlow Tower<br>12th Floor Avondale, Ohio 43020</span>
      </div>
      <div class="contact__row">
        <svg class="contact__icon" viewBox="0 0 12 12"><path d="M2.5 0.5l2 2.5-1.2 1.3a7 7 0 0 0 4.4 4.4L9 7.5l2.5 2-1.2 2C5 11.5 0.5 7 0.5 1.7z"/></svg>
        <span>+614-555-0182</span>
      </div>
      <div class="contact__row">
        <svg class="contact__icon" viewBox="0 0 12 12"><path d="M0.5 2h11v8h-11zM1.5 3l4.5 3.5L10.5 3v-0.2h-9z" fill-rule="evenodd"/></svg>
        <span>info@meridell.us</span>
      </div>
    </div>

    <div class="band band--left"></div>
    <p class="website">www.meridell.us</p>
    <div class="band band--right"></div>
  </section>
</body>
</html>
```